Serene Path website development

Need a website designed for a coaching business. Very high-end, luxury, professionalism, in the area of STRESS, see brief attached. I have a logo already
Updates

Slow in providing feedback

Target Market(s)

CEOs very successful men and wealthy females, high end luxury market

Industry/Entity Type

coaching

Number of Pages Required

1 page

Requirements
Must have
• Luxury look, professional, serious but warm, appealing to both sexes

```html
<!DOCTYPE html>
<html lang="en">
<head>
<meta charset="utf-8">
<title>Serene Path — Executive Stress Coaching</title>
<link href="https://fonts.googleapis.com/css2?family=Playfair+Display:wght@400;700&family=Roboto+Slab:wght@300;400&family=Mulish:wght@400;700;800&family=Oswald:wght@300&display=swap" rel="stylesheet">
<style>
:root{
  --ink:#111111;
  --black:#000000;
  --white:#ffffff;
  --slate:#20252b;
  --charcoal:#1b1b1c;
  --navy:#262d40;
  --field:#ebebeb;
  --muted:#555555;
  --accent:#2a8fd8;
  --light-text:#d9dbe0;
}
*{box-sizing:border-box;margin:0;padding:0}
html,body{width:1200px;height:3400px;overflow:hidden}
body{position:relative;background:var(--white);font-family:"Roboto Slab",serif;color:var(--ink)}
.abs{position:absolute}
.brand{font-family:"Mulish",sans-serif;font-weight:800;letter-spacing:4px;text-transform:uppercase}

/* top bar */
.topbar{left:0;top:0;width:1200px;height:21px;background:var(--black);color:var(--white);font:400 10px/21px "Mulish",sans-serif}
.topbar .call{left:129px}
.topbar .socials{right:129px;top:5px;display:flex;gap:9px}
.topbar .socials span{width:10px;height:10px;border:1.5px solid var(--white);border-radius:2px}

/* nav */
.nav{left:0;top:21px;width:1200px;height:64px;background:var(--white)}
.nav .logo{left:129px;top:26px;font-size:12px;display:flex;align-items:center;gap:8px}
.nav .logo i{width:12px;height:12px;border-radius:50%;background:var(--ink);display:block}
.nav ul{list-style:none;right:129px;top:24px;display:flex;gap:40px;font:400 11.5px "Mulish",sans-serif}
.nav li.active{color:var(--accent);border-bottom:1px solid var(--accent);padding-bottom:3px}

/* hero */
.hero{left:0;top:85px;width:1200px;height:414px;background:linear-gradient(90deg,#3f4a3b 0%,#5f6b54 35%,#7a8164 60%,#4d5343 100%)}
.hero .photo{inset:0;background:radial-gradient(ellipse at 78% 55%,rgba(20,20,20,.75) 0 22%,transparent 45%),linear-gradient(180deg,rgba(255,255,255,.08),rgba(0,0,0,.25))}
.hero h1{left:130px;top:88px;font:700 80px/78px "Playfair Display",serif;color:var(--white)}
.hero h1 span{font-weight:400}
.hero .dots{left:570px;top:395px;display:flex;gap:4px}
.hero .dots i{width:17px;height:2px;background:rgba(255,255,255,.55);display:block}
.hero .dots i:first-child{background:var(--white)}

/* buttons */
.btn{display:flex;align-items:center;padding-left:24px;font:400 11px "Roboto Slab",serif;text-transform:uppercase;position:absolute}
.btn::after{content:"";position:absolute;right:0;top:0;width:18px;height:100%;background:repeating-linear-gradient(135deg,#b9b9b9 0 2px,transparent 2px 5px)}
.btn.light{background:var(--white);color:var(--ink)}
.btn.dark{background:var(--ink);color:var(--white)}
.btn.dark::after{background:repeating-linear-gradient(135deg,#777 0 2px,transparent 2px 5px)}

/* welcome */
.welcome-panel{left:0;top:499px;width:429px;height:536px;background:var(--black)}
.welcome-label{left:40px;top:565px;width:48px;height:80px;color:var(--white);font:300 21px "Oswald",sans-serif;letter-spacing:1px;writing-mode:vertical-rl;transform:rotate(180deg);display:flex;align-items:center;justify-content:center}
.welcome-rule{left:64px;top:668px;width:1px;height:334px;background:var(--white)}
.welcome-photo{left:129px;top:564px;width:381px;height:408px;background:linear-gradient(120deg,#c24a2e 0%,#9c3b28 30%,#3a3f4d 55%,#6e7c93 80%,#cbbfae 100%)}
.welcome-copy{left:610px;top:624px;width:460px}
.welcome-copy .kicker{font:400 18px "Roboto Slab",serif}
.welcome-copy h2{font:400 45px/56px "Playfair Display",serif;margin-top:4px}
.welcome-copy p{margin-top:19px;font:300 13.5px/20px "Roboto Slab",serif;color:#333}

/* audience */
.audience{left:0;top:1035px;width:1200px;height:606px;background:radial-gradient(ellipse at 30% 70%,#2a3038,var(--slate) 70%)}
.audience .card-photo{top:62px;width:460px;height:294px;border-radius:8px}
.audience .men{left:129px;background:linear-gradient(110deg,#e6e9ec 0%,#b8bec4 40%,#7b8189 65%,#c9ccd0 100%)}
.audience .women{left:610px;background:linear-gradient(100deg,#3c4a2f 0%,#6b6f5f 30%,#b4a89a 55%,#e7e5e2 100%)}
.audience h3{top:370px;width:460px;text-align:center;color:var(--white);font:400 34px/44px "Playfair Display",serif}
.audience p{top:426px;width:420px;text-align:center;color:var(--light-text);font:300 13px/20px "Roboto Slab",serif}

/* why me */
.why-photo{left:129px;top:1680px;width:316px;height:408px;clip-path:polygon(38% 0,100% 8%,100% 70%,53% 100%,0 88%,0 25%);background:linear-gradient(150deg,#6d8e3e 0%,#a6b98a 35%,#e2ddd6 60%,#bcb4ab 100%)}
.why h2{left:515px;top:1752px;font:400 40px "Playfair Display",serif}
.why ul{left:515px;top:1829px;width:545px;list-style:none;font:300 13.5px/20px "Roboto Slab",serif;color:#333}
.why li{position:relative;padding-left:15px;margin-bottom:20px}
.why li::before{content:"+";position:absolute;left:0;top:0;font-weight:400}

/* benefits */
.benefits{left:0;top:2149px;width:1200px;height:521px;background:var(--charcoal);overflow:hidden}
.benefits h2{top:28px;width:1200px;text-align:center;color:var(--white);font:400 42px "Playfair Display",serif}
.benefit{width:220px;text-align:center;color:var(--white);font:700 19px "Playfair Display",serif}
.benefit svg{display:block;margin:0 auto 6px}
.hub-name{left:450px;top:470px;width:300px;text-align:center;color:var(--white);font-size:19px;letter-spacing:6px}

/* contact */
.contact h2{top:2748px;width:1200px;text-align:center;font:400 42px "Playfair Display",serif}
.field{background:var(--field);font:400 10px "Roboto Slab",serif;color:#444;display:flex;align-items:center;gap:5px;padding-left:8px}
.field.msg{align-items:flex-start;padding-top:11px}
.submit{left:603px;top:2932px;width:272px;height:35px;background:var(--ink);color:var(--white);font:400 12px "Roboto Slab",serif;display:flex;align-items:center;justify-content:center;gap:6px}

/* footer */
.footer{left:0;top:3056px;width:1200px;height:344px;background:var(--navy);color:var(--white)}
.footer .logo{left:130px;top:175px;width:290px;text-align:center;font-size:23px;letter-spacing:7px}
.footer .copyright{left:130px;top:219px;font:400 11px "Roboto Slab",serif}
.footer .col{top:96px;border-left:2px solid var(--white);padding-left:20px;height:160px}
.footer .col h4{font:700 15px "Playfair Display",serif;margin-bottom:16px}
.footer .col ul{list-style:none;font:400 11px/21px "Roboto Slab",serif}
.footer .contact-col li{display:flex;gap:4px;margin-bottom:26px;line-height:14px}
.footer .ring{width:26px;height:26px;border:1.5px solid var(--white);border-radius:50%;display:inline-block;margin-right:5px}
</style>
</head>
<body>

<header class="abs topbar">
  <span class="abs call">Call Us: +1 (555) 204 7731</span>
  <div class="abs socials"><span></span><span></span><span></span></div>
</header>

<nav class="abs nav">
  <div class="abs logo brand"><i></i>Serene Path</div>
  <ul class="abs">
    <li class="active">Home</li><li>About Us</li><li>Services</li><li>Benefits</li><li>Blog</li><li>Contact Us</li>
  </ul>
</nav>

<section class="abs hero">
  <div class="abs photo" role="img" aria-label="Woman in black relaxing in a chair by a lake, holding a coffee cup"></div>
  <h1 class="abs">Head Coach<br><span>Get it!</span></h1>
  <a class="btn light" style="left:132px;top:278px;width:114px;height:33px">Read More</a>
  <div class="abs dots"><i></i><i></i><i></i></div>
</section>

<section class="welcome">
  <div class="abs welcome-panel"></div>
  <div class="abs welcome-label">WELCOME</div>
  <div class="abs welcome-rule"></div>
  <div class="abs welcome-photo" role="img" aria-label="Coach in conversation with a distressed client on a sofa"></div>
  <div class="abs welcome-copy">
    <div class="kicker">Welcome To</div>
    <h2>Serene Path</h2>
    <p>Serene Path came about due to my desire to help people lead a better and healthier life. Initially, I was involved in the fitness/body side of health. As years passed and my experience grew, I realized how important the mind was in total wellness, and that the mind is all powerful and controlling. Control the mind, control the body and achieve success. Stress can be the most debilating factor...</p>
  </div>
  <a class="btn dark" style="left:610px;top:871px;width:115px;height:35px">Read More</a>
</section>

<section class="abs audience">
  <div class="abs card-photo men" role="img" aria-label="Stressed businessman at his desk holding his head"></div>
  <div class="abs card-photo women" role="img" aria-label="Woman drinking coffee at a bright office desk"></div>
  <h3 class="abs" style="left:129px">MEN</h3>
  <h3 class="abs" style="left:610px">WOMEN</h3>
  <p class="abs" style="left:149px">The stress of success...they cannot share with anyone in fear of showing weakness...or a chink in the armor...not fully fulfilled, will provide and/or sign a confidentiality agreement.</p>
  <p class="abs" style="left:630px">General issues...I live near very wealthy neighborhoods with lots of "trophy wives" who are really quite lonely, as husbands work a great deal.</p>
  <a class="btn light" style="left:293px;top:509px;width:133px;height:32px;padding-left:21px">Men Click Here</a>
  <a class="btn light" style="left:772px;top:509px;width:148px;height:32px;padding-left:20px">Women Click Here</a>
</section>

<section class="why">
  <div class="abs why-photo" role="img" aria-label="Portrait of the head coach smiling outdoors"></div>
  <h2 class="abs">Why Me</h2>
  <ul class="abs">
    <li>Been there done that! Have been through a lot, started businesses, selling a business, law suits, marriage, divorce, second marriage, kids, school, sports, fights, robbed, gun in face, traveled the world, successful, two great kids (both Cadets at Ridgecrest Academy...duty/honor/country)</li>
    <li>Limited number of clients...different stage of life, empty nester, have a full career...won't be a number</li>
  </ul>
  <a class="btn dark" style="left:515px;top:2000px;width:115px;height:33px">Read More</a>
</section>

<section class="abs benefits">
  <svg class="abs" style="left:0;top:0" width="1200" height="521" viewBox="0 0 1200 521">
    <defs>
      <linearGradient id="ray" x1="0" y1="1" x2="0" y2="0">
        <stop offset="0" stop-color="#fff" stop-opacity=".14"/>
        <stop offset="1" stop-color="#fff" stop-opacity="0"/>
      </linearGradient>
    </defs>
    <polygon points="600,521 80,0 330,0" fill="url(#ray)"/>
    <polygon points="600,521 520,0 700,0" fill="url(#ray)"/>
    <polygon points="600,521 860,0 1060,0" fill="url(#ray)"/>
    <polygon points="600,521 0,330 0,420" fill="url(#ray)"/>
    <polygon points="600,521 1200,300 1200,380" fill="url(#ray)"/>
    <path d="M425,521 A175,175 0 0 1 470,390 L600,521 Z" fill="#3a3a3a"/>
    <path d="M470,390 A182,182 0 0 1 640,340 L600,521 Z" fill="#4a4a4a"/>
    <path d="M640,340 A195,195 0 0 1 755,400 L600,521 Z" fill="#6a6a6a"/>
    <path d="M755,400 A210,210 0 0 1 795,521 L600,521 Z" fill="#9a9a9a"/>
    <circle cx="600" cy="521" r="160" fill="#000"/>
    <g fill="#fff" font-family="Playfair Display, serif" font-size="18">
      <text x="445" y="436">1</text><text x="530" y="362">2</text><text x="641" y="359">3</text>
      <text x="730" y="422">4</text><text x="770" y="512">5</text>
    </g>
  </svg>
  <h2 class="abs">Our Benefits</h2>

  <div class="abs benefit" style="left:509px;top:134px">
    <svg width="50" height="50" viewBox="0 0 50 50" fill="none" stroke="#fff" stroke-width="2"><circle cx="28" cy="15" r="8"/><path d="M18 15a10 10 0 0 1 20 0"/><path d="M14 46v-8a14 10 0 0 1 28 0v8"/><rect x="4" y="28" width="12" height="14"/></svg>
    Excellent Listener
  </div>
  <div class="abs benefit" style="left:314px;top:195px">
    <svg width="60" height="60" viewBox="0 0 60 60" fill="none" stroke="#fff" stroke-width="2"><circle cx="30" cy="14" r="5"/><path d="M30 20v16M22 56l6-20M38 56l-6-20M12 12l10 14 8-4 8 4 10-14"/></svg>
    Sector Expert Health
  </div>
  <div class="abs benefit" style="left:715px;top:210px">
    <svg width="52" height="40" viewBox="0 0 52 40" fill="none" stroke="#fff" stroke-width="2"><circle cx="26" cy="18" r="8"/><circle cx="6" cy="8" r="4"/><circle cx="46" cy="8" r="4"/><circle cx="6" cy="32" r="4"/><circle cx="46" cy="32" r="4"/><path d="M10 10l9 5M42 10l-9 5M10 30l9-6M42 30l-9-6"/></svg>
    Access
  </div>
  <div class="abs benefit" style="left:140px;top:380px">
    <svg width="66" height="46" viewBox="0 0 66 46" fill="none" stroke="#fff" stroke-width="2"><circle cx="33" cy="8" r="6"/><path d="M33 18l4 8 9 1-7 6 2 9-8-5-8 5 2-9-7-6 9-1z"/><circle cx="8" cy="22" r="3"/><circle cx="58" cy="22" r="3"/><circle cx="14" cy="36" r="3"/><circle cx="52" cy="36" r="3"/></svg>
    Experience
  </div>
  <div class="abs benefit" style="left:818px;top:378px">
    <svg width="50" height="52" viewBox="0 0 50 52" fill="none" stroke="#fff" stroke-width="2"><path d="M25 3l19 7v14c0 14-9 22-19 26C15 46 6 38 6 24V10z"/><circle cx="25" cy="22" r="6"/><path d="M15 40a10 8 0 0 1 20 0"/></svg>
    Private
  </div>
  <div class="abs hub-name brand">Serene Path</div>
</section>

<section class="contact">
  <h2 class="abs">Contact Serene Path</h2>
  <div class="abs field" style="left:323px;top:2831px;width:274px;height:36px">
    <svg width="10" height="10" viewBox="0 0 10 10" fill="none" stroke="#444"><circle cx="5" cy="3" r="2.2"/><path d="M1 10a4 4 0 0 1 8 0"/></svg>Name:
  </div>
  <div class="abs field" style="left:323px;top:2882px;width:274px;height:35px">
    <svg width="11" height="9" viewBox="0 0 11 9" fill="none" stroke="#444"><rect x=".5" y=".5" width="10" height="8"/><path d="M.5 .5l5 4 5-4"/></svg>Email:
  </div>
  <div class="abs field" style="left:323px;top:2932px;width:274px;height:35px">
    <svg width="10" height="10" viewBox="0 0 10 10" fill="none" stroke="#444"><path d="M2 1l2 2-1 1.5c.8 1.5 1.5 2.2 3 3L7.5 6l2 2-1.5 1.5C4 9 1 6 .5 2z"/></svg>Phone:
  </div>
  <div class="abs field msg" style="left:603px;top:2831px;width:272px;height:85px">
    <svg width="11" height="11" viewBox="0 0 11 11" fill="none" stroke="#444"><path d="M5.5 1C8.3 1 10 2.8 10 5s-1.7 4-4.5 4c-.8 0-1.5-.1-2-.4L1 9.8l.9-2C1.3 7 1 6 1 5 1 2.8 2.7 1 5.5 1z"/></svg>Message:
  </div>
  <div class="abs submit">
    <svg width="11" height="11" viewBox="0 0 11 11" fill="#fff"><path d="M0 5l11-5-3 11-3-4-5-2z"/></svg>Submit
  </div>
</section>

<footer class="abs footer">
  <div class="abs logo brand">Serene Path</div>
  <p class="abs copyright">Copyright © 2022 Serene Path. All Rights Reserved.</p>

  <div class="abs col contact-col" style="left:510px;width:250px">
    <h4>Contact Us</h4>
    <ul>
      <li><svg width="9" height="11" viewBox="0 0 10 10" fill="#fff"><path d="M2 1l2 2-1 1.5c.8 1.5 1.5 2.2 3 3L7.5 6l2 2-1.5 1.5C4 9 1 6 .5 2z"/></svg>+1 (555) 204 7731</li>
      <li><svg width="10" height="11" viewBox="0 0 11 9" fill="#fff"><rect width="11" height="8" y=".5"/></svg>hello@serenepath.example</li>
      <li><svg width="9" height="12" viewBox="0 0 9 12" fill="#fff"><path d="M4.5 0A4.5 4.5 0 0 0 0 4.5C0 8 4.5 12 4.5 12S9 8 9 4.5A4.5 4.5 0 0 0 4.5 0zm0 6.3a1.8 1.8 0 1 1 0-3.6 1.8 1.8 0 0 1 0 3.6z"/></svg>42 Harbor Lane, Suite 7,<br>Lakeview 20418 USA</li>
    </ul>
  </div>

  <div class="abs col" style="left:775px;width:160px">
    <h4>Navigation</h4>
    <ul><li>Home</li><li>About Us</li><li>Services</li><li>Benefits</li><li>Blog</li><li>Contact Us</li></ul>
  </div>

  <div class="abs col" style="left:950px;width:140px;height:60px;padding-left:22px">
    <h4>Follow Us</h4>
    <div><span class="ring"></span><span class="ring"></span><span class="ring"></span></div>
  </div>
</footer>

</body>
</html>
```